Holiday Party Flyer Template

We are a company offering downloadable flyer designs to customers. We are seeking to broaden our design categories and would like to start with the party invitation category and in specific a Holiday themed party. There will be one winner but we will be following up with all designers who we feel have submitted quality work to discuss potentially licensing your designs so this could lead to much more work even if you dont win the contest. Please consider the following requirements and instructions:

* Holiday Party Flyer Design (Winter theme suitable for any small to large holdiay party event)

* Text elements to include: Event title, event location, event time and date, room for 2 to 3 paragraphs of text such as for attire, directions etc. Room for a company logo - note that the design should still look good if there is NOT a company logo since this may or may not be used by our client. Placeholder text can be used at the designers discretion in all areas described above. For example, you can feel free to call it "Winter Holiday Party" or "Annual Company Holiday Bash", etc. Its up to you - be creative.

* Design for letter size paper (8.5" by 11" 300dpi vector based!)

* If you only submit a single design, make sure the design does not contain anything specific to a certain religion (ie, Santa Claus, mangers and wise men or anything like that)

* Some of our clients may want to use the flyer design for Christmas or Hanukah themed events, so if you submit multiple designs, please feel free to include elements relating to these themes such as Santa and so on.

```html
<!DOCTYPE html>
<html lang="en">
<head>
<meta charset="utf-8">
<title>Annual Company Holiday Bash</title>
<link rel="stylesheet" href="https://fonts.googleapis.com/css2?family=Almendra:wght@700&family=Titan+One&family=Archivo:wght@700;800&display=swap">
<style>
  :root {
    --backdrop: #e9e3dc;
    --wine-dark: #3a0608;
    --wine: #6e0c10;
    --crimson: #c4141a;
    --scarlet: #e3201f;
    --gold: #f2c95a;
    --gold-deep: #b8862e;
    --band: #0d0a0a;
    --holly: #5fcf2c;
    --holly-dark: #1d5a0c;
    --snow: #ffffff;
  }
  * { margin: 0; padding: 0; box-sizing: border-box; }
  html, body { width: 1200px; height: 606px; overflow: hidden; background: var(--backdrop); }
  .canvas { position: relative; width: 1200px; height: 606px; }

  .flyer {
    position: absolute; left: 379px; top: 18px; width: 442px; height: 571px;
    background: linear-gradient(180deg, var(--wine-dark) 0%, var(--wine) 30%, var(--crimson) 60%, var(--scarlet) 82%);
    font-family: "Archivo", "Arial", sans-serif; font-weight: 800; text-align: center;
    overflow: hidden; box-shadow: 0 4px 14px rgba(0,0,0,.35);
  }
  .corner { position: absolute; width: 30px; height: 30px; border: 2px solid var(--gold-deep); }
  .corner--tl { left: 14px; top: 14px; border-right: 0; border-bottom: 0; }
  .corner--tr { right: 14px; top: 14px; border-left: 0; border-bottom: 0; }
  .corner--bl { left: 14px; bottom: 14px; border-right: 0; border-top: 0; }
  .corner--br { right: 14px; bottom: 14px; border-left: 0; border-top: 0; }

  .event-date { position: absolute; top: 22px; width: 100%; color: var(--gold); font-size: 14px; line-height: 15px; }
  .divider { position: absolute; left: 136px; top: 66px; width: 170px; height: 2px; background: var(--gold-deep); }
  .divider-art { position: absolute; left: 196px; top: 70px; width: 50px; height: 26px; border-radius: 50%;
    background: radial-gradient(var(--gold) 0%, var(--gold-deep) 60%, transparent 70%); opacity: .8; }
  .presenter { position: absolute; top: 108px; width: 100%; color: var(--gold); font-size: 8.5px; }

  .title-art { position: absolute; left: 30px; top: 134px; width: 382px; height: 244px; border-radius: 40%;
    background: radial-gradient(ellipse at 50% 55%, #ffd97a 0%, #d59a35 35%, rgba(150,20,20,.6) 65%, transparent 75%); }

  .title { position: absolute; top: 148px; width: 100%; }
  .title-line { display: block; }
  .title-annual, .title-bash {
    font-family: "Almendra", "Georgia", serif; font-weight: 700; color: var(--snow);
    text-shadow: 0 2px 0 #888, 0 3px 6px rgba(0,0,0,.7);
  }
  .title-annual { font-size: 54px; line-height: 60px; }
  .title-company {
    font-family: "Titan One", "Arial Black", sans-serif; color: var(--holly); font-size: 44px; line-height: 44px; letter-spacing: 1px;
    text-shadow: 0 0 2px var(--holly-dark), 0 2px 0 var(--holly-dark), 0 4px 6px rgba(0,0,0,.6);
  }
  .title-bash { font-size: 58px; line-height: 66px; }

  .details { position: absolute; top: 398px; width: 100%; color: var(--gold); }
  .details-lead { font-size: 7.5px; line-height: 9px; }
  .details-head { font-size: 12.5px; line-height: 15px; margin-top: 1px; }
  .details-body { font-size: 5.5px; line-height: 6.6px; margin: 3px auto 0; width: 280px; }

  .footer-band { position: absolute; left: 0; bottom: 0; width: 100%; height: 102px; background: var(--band); }
  .sponsors { position: absolute; top: 30px; left: 0; width: 100%; display: flex; justify-content: center; align-items: center; gap: 18px; }
  .sponsor { color: var(--snow); font-size: 8px; font-weight: 700; display: flex; align-items: center; gap: 4px; }
  .sponsor-dot { width: 9px; height: 9px; border-radius: 50%; background: var(--scarlet); }
  .contact { position: absolute; top: 67px; width: 100%; color: var(--gold); font-size: 9px; }
</style>
</head>
<body>
<main class="canvas">
  <article class="flyer">
    <span class="corner corner--tl"></span>
    <span class="corner corner--tr"></span>

    <p class="event-date">SUNDAY | 12.21.10<br>9:00AM-6:00</p>
    <span class="divider"></span>
    <span class="divider-art" role="img" aria-label="Gold scroll ornament"></span>
    <p class="presenter">LOREM IPSUM DOLOR SIT AMET PRESENTS</p>

    <div class="title-art" role="img" aria-label="Gold ribbons, bells and red bow behind the title"></div>
    <h1 class="title">
      <span class="title-line title-annual">Annual</span>
      <span class="title-line title-company">COMPANY</span>
      <span class="title-line title-bash">Holiday Bash</span>
    </h1>

    <section class="details">
      <p class="details-lead">LOREM IPSUM DOLOR SIT AMET<br>ARCU A JUSTO, DOLOR SEM</p>
      <p class="details-head">AENEAN FERMENTUM</p>
      <p class="details-body">LOREM IPSUM DOLOR SIT AMET, ARCU A JUSTO, DOLOR SEM AENEAN FERMENTUM AT EU UT AMET SUSPENDISSE VESTIBULUM. UT FUSCE FAUCIBUS ALIQUAM PULVINAR INTEGER AUGUE VESTIBULUM MAGNA AC IPSUM SCELERISQUE NIBH, EU UT DIGNISSIM AMET INTEGER NULLAM LACUS, SEMPER MASSA LOBORTIS QUIS ET NUNC VITAE</p>
    </section>

    <footer class="footer-band">
      <div class="sponsors">
        <span class="sponsor"><span class="sponsor-dot"></span>Birchway</span>
        <span class="sponsor">Loft Hall</span>
        <span class="sponsor"><span class="sponsor-dot"></span>Turnabout</span>
        <span class="sponsor">Kettle Bell Productions</span>
        <span class="sponsor">Noria</span>
      </div>
      <p class="contact">LOREM IPSUM DOLOR SIT AMET 0123456789</p>
    </footer>

    <span class="corner corner--bl"></span>
    <span class="corner corner--br"></span>
  </article>
</main>
</body>
</html>
```